Pellrow Strategies business card

I need a business card for my new strategic consulting LLC, Pellrow Strategies. We specialize in helping people who care about broadband technology and telecommunications policy, and we're based in Washington DC. I'm looking for a card that says smart, credible, future-facing and signals a high level of expertise. It's DC, so there's clearly a limit to how crazy we can go with this card, but I am looking for a design that reflects a company that is comfortable with technology, policy, and having a little bit fun. I'm uploading my logo below, and I'd like to have it be part of the card design in some fashion.
Target Market(s)
Telecommunications and technology policy professionals
Industry/Entity Type
Technology policy
Contact Information for Business Card
Name of business, my name (Colin Mabberly), email (colin@pellrowstrategies.example) , phone number (202-555-0148)phone number
Look and feel

```html
<!DOCTYPE html>
<html lang="en">
<head>
<meta charset="utf-8">
<title>Pellrow Strategies – Business Card</title>
<link href="https://fonts.googleapis.com/css2?family=Montserrat:wght@400;500;700;800&display=swap" rel="stylesheet">
<style>
  :root {
    --backdrop: #d4d5d8;
    --navy: #1d3f8a;
    --navy-deep: #141d3f;
    --night: #1b2c66;
    --glow-blue: #2f55b8;
    --ember: #c8643a;
    --orange: #f0a33a;
    --ink: #1c1c1c;
    --paper: #ffffff;
  }
  * { box-sizing: border-box; margin: 0; padding: 0; }
  html, body {
    width: 1200px; height: 800px; overflow: hidden;
    background: var(--backdrop);
    font-family: "Montserrat", Arial, sans-serif;
  }
  .stage { position: relative; width: 1200px; height: 800px; }

  .card {
    position: absolute;
    width: 525px; height: 300px;
    box-shadow: 0 14px 30px rgba(0,0,0,0.22);
    overflow: hidden;
  }

  /* Front */
  .card-front { left: 45px; top: 110px; }
  .front-field {
    position: absolute; inset: 0;
    background:
      radial-gradient(ellipse 60% 40% at 88% 85%, rgba(200,100,58,0.55), transparent 70%),
      radial-gradient(ellipse 55% 60% at 75% 30%, var(--glow-blue), transparent 75%),
      linear-gradient(135deg, var(--navy-deep) 0%, var(--night) 55%, #23398a 100%);
  }
  .front-wordmark {
    position: absolute; inset: 0;
    display: flex; align-items: center; justify-content: center;
    color: var(--paper);
    font-weight: 700; font-size: 40px; letter-spacing: 0.5px;
  }

  /* Back */
  .card-back { left: 630px; top: 380px; background: var(--paper); }
  .brand {
    position: absolute; right: 30px; top: 30px;
    display: flex; flex-direction: column; align-items: flex-end;
  }
  .brand-dot {
    width: 62px; height: 62px; border-radius: 50%;
    background: var(--orange); margin-bottom: 14px;
  }
  .brand-name {
    color: var(--navy); font-weight: 700; font-size: 34px;
    line-height: 1.1; text-align: right;
  }
  .contact { position: absolute; left: 30px; top: 112px; }
  .contact-name {
    color: var(--navy); font-weight: 800; font-size: 28px; line-height: 1.1;
  }
  .contact-role { color: var(--ink); font-size: 15px; margin-top: 4px; }
  .contact-rule {
    width: 95px; height: 3px; background: var(--orange); margin: 8px 0 10px;
  }
  .contact-list { list-style: none; }
  .contact-list li {
    display: flex; align-items: center; gap: 8px;
    color: var(--ink); font-size: 14px; line-height: 26px;
  }
  .contact-list svg { width: 13px; height: 13px; fill: var(--orange); flex: none; }
  .base-band {
    position: absolute; left: 0; right: 0; bottom: 0; height: 10px; background: var(--navy);
  }
</style>
</head>
<body>
<main class="stage">
  <section class="card card-front">
    <div class="front-field" role="img" aria-label="Deep blue starfield with glowing connected network nodes and a warm orange light streak"></div>
    <div class="front-wordmark">Pellrow Strategies</div>
  </section>

  <section class="card card-back">
    <div class="brand">
      <div class="brand-dot"></div>
      <div class="brand-name">Pellrow<br>Strategies</div>
    </div>
    <div class="contact">
      <h1 class="contact-name">Colin Mabberly</h1>
      <p class="contact-role">Director</p>
      <div class="contact-rule"></div>
      <ul class="contact-list">
        <li>
          <svg viewBox="0 0 24 24" aria-hidden="true"><path d="M6.6 10.8a15.1 15.1 0 0 0 6.6 6.6l2.2-2.2c.3-.3.7-.4 1-.2 1.1.4 2.3.6 3.6.6.6 0 1 .4 1 1V20c0 .6-.4 1-1 1A17 17 0 0 1 3 4c0-.6.4-1 1-1h3.5c.6 0 1 .4 1 1 0 1.3.2 2.5.6 3.6.1.3 0 .7-.2 1z"/></svg>
          202-555-0148
        </li>
        <li>
          <svg viewBox="0 0 24 24" aria-hidden="true"><path d="M2 5h20v14H2z M2 5l10 8 10-8" fill="none" stroke="#f0a33a" stroke-width="2.2"/></svg>
          colin@pellrowstrategies.example
        </li>
        <li>
          <svg viewBox="0 0 24 24" aria-hidden="true"><g fill="none" stroke="#f0a33a" stroke-width="2"><circle cx="12" cy="12" r="9"/><path d="M3 12h18M12 3c3 3 3 15 0 18M12 3c-3 3-3 15 0 18"/></g></svg>
          pellrowstrategies.example
        </li>
      </ul>
    </div>
    <div class="base-band"></div>
  </section>
</main>
</body>
</html>
```